Banner for Vet Hospital 5m x 1.2m - Heat Stroke

Meadowlark Pet Hospital needs a Heat Stroke Banner for Summer.
The banner will be 5000mm long and 1200mm tall.

Our region has been hot this year and this summer is going to be extremely hot.
I want to warn people about heat stroke.
I want you to create a heat stroke banner that conveys the symptoms of heat stroke.

Pictures are better than words.
There should be IMAGES and WORDS that can be seen from the road 30m away and maybe some smaller words for people to read as they walk past.

Here are some of the signs of Heat Stroke:
- Panting which increases as heatstroke progresses
- Drooling, salivating
- Agitation, restlessness
- Very red or pale gums
- Bright red tongue
- Increased heart rate
- Breathing distress
- Vomiting Diarrhea (possibly with blood)
- Signs of mental confusion, delirium
- Dizziness, staggering
- Lethargy, weakness
- Muscle tremors
- Seizures
- Collapsing and lying down
- Little to no urine production
- Coma

I have attached characters that we often use in our advertising. They are optional.
I have done a mock up of the design I imagine. You could refine this design or make your own....or both.

Target Market(s)

Women aged 20 to 50.

Industry/Entity Type

Veterinary

Font styles to use
Sans Serif

Colors
fbed22
f78f20
ec1f27
ffffff

Requirements
Must have
• Heat Stroke Symtpms.
• Heat Stroke Warning.
• Summer theme.
Nice to have
• Bright colours.

```html
<!DOCTYPE html>
<html lang="en">
<head>
<meta charset="utf-8">
<title>Heat Stroke Banner – Meadowlark Pet Hospital</title>
<link rel="stylesheet" href="https://fonts.googleapis.com/css2?family=Archivo+Black&family=Courgette&family=Roboto:wght@400;500;700;900&display=swap">
<style>
  :root {
    --sun-yellow: #f7ea2b;
    --heat-orange: #f78f20;
    --alert-red: #ec1f27;
    --ink: #111111;
    --paper: #ffffff;
    --stage: #dcdcdc;
    --photo-warm: #d9a46a;
    --photo-soft: #c99a78;
  }
  html, body {
    margin: 0;
    width: 1200px;
    height: 1200px;
    overflow: hidden;
    background: var(--stage);
  }
  .canvas {
    width: 1200px;
    height: 1200px;
    display: flex;
    align-items: center;
    justify-content: center;
  }
  .banner {
    width: 1140px;
    height: 273px;
    display: block;
    box-shadow: 0 6px 18px rgba(0,0,0,0.25);
  }
  .headline { font-family: "Archivo Black", sans-serif; font-size: 32px; fill: var(--ink); }
  .script { font-family: "Courgette", cursive; fill: var(--paper); }
  .question { font-size: 30px; }
  .symptom { font-size: 20px; }
  .tagline { font-family: "Roboto", sans-serif; font-weight: 700; font-size: 15px; fill: var(--heat-orange); }
  .know { font-family: "Roboto", sans-serif; font-weight: 500; font-size: 14px; fill: var(--ink); }
  .cta { font-family: "Roboto", sans-serif; font-weight: 500; font-size: 22px; fill: var(--paper); }
  .web { font-family: "Roboto", sans-serif; font-weight: 700; font-size: 15px; fill: var(--ink); }
  .phone { font-family: "Roboto", sans-serif; font-weight: 900; font-size: 52px; fill: var(--sun-yellow); }
  .brand { font-family: "Roboto", sans-serif; font-weight: 500; fill: #6b4a2e; }
</style>
</head>
<body>
<main class="canvas">
  <svg class="banner" viewBox="0 0 1335 320" xmlns="http://www.w3.org/2000/svg">
    <!-- base fields -->
    <rect class="field-yellow" width="1335" height="320" fill="var(--sun-yellow)"/>
    <polygon class="field-orange" points="635,0 830,0 760,320 560,320" fill="var(--heat-orange)"/>
    <polygon class="field-white" points="830,0 1335,0 1335,320 760,320" fill="var(--paper)"/>
    <polygon class="accent-stripe" points="1205,0 1218,0 1128,320 1115,320" fill="var(--sun-yellow)"/>

    <!-- photo frames -->
    <polygon points="20,12 372,12 340,240 5,240" fill="var(--heat-orange)"/>
    <polygon role="img" aria-label="Photo of a puppy high-fiving a woman on a sunny beach" points="26,18 364,18 334,234 12,234" fill="var(--photo-warm)"/>
    <polygon points="298,86 592,86 570,300 262,300" fill="var(--heat-orange)"/>
    <polygon role="img" aria-label="Photo of a woman hugging her dog" points="305,93 584,93 563,293 270,293" fill="var(--photo-soft)"/>

    <!-- question and symptoms -->
    <text class="script question" x="640" y="64">Is your Dog</text>
    <g class="symptoms">
      <text class="script symptom" x="620" y="113">✓ Panting</text>
      <text class="script symptom" x="610" y="147">✓ Loosing Breath</text>
      <text class="script symptom" x="600" y="181">✓ Not Eating</text>
      <text class="script symptom" x="592" y="215">✓ Restless?</text>
    </g>

    <!-- headline -->
    <polygon class="headline-bar" points="826,20 1312,20 1296,78 812,78" fill="var(--sun-yellow)"/>
    <text class="headline" x="842" y="63">Prevent a Heat Stroke !</text>

    <text class="tagline" x="825" y="101">Lets get together and help your loving dog</text>
    <text class="tagline" x="820" y="119">strive this Hot Summer !</text>
    <text class="know" x="815" y="144">Get to know:</text>
    <text class="know" x="808" y="165">⚠ Precautions</text>
    <text class="know" x="930" y="165">? Symptoms</text>
    <text class="know" x="1043" y="165">◌ Solutions</text>

    <!-- call to action -->
    <polygon class="cta-box" points="800,182 1130,182 1118,240 786,240" fill="var(--heat-orange)"/>
    <text class="cta" x="843" y="207">BOOK ONLINE NOW</text>
    <circle cx="815" cy="225" r="7" fill="none" stroke="var(--ink)" stroke-width="1.6"/>
    <text class="web" x="832" y="230">www.meadowlarkpethospital.com.au</text>

    <!-- phone bar -->
    <polygon class="phone-bar" points="550,248 1137,248 1122,308 537,308" fill="var(--ink)"/>
    <g class="phone-icon" fill="none" stroke="var(--sun-yellow)" stroke-width="3.5">
      <circle cx="635" cy="279" r="18"/>
      <path d="M627 270 q-2 12 8 18 l4 -3 -4 -5 -3 2 q-3 -3 -3 -7 l3 -1 -2 -6 z" fill="var(--sun-yellow)" stroke-width="1"/>
    </g>
    <text class="phone" x="682" y="298">02 5550 1947</text>

    <!-- hospital name -->
    <circle cx="1252" cy="178" r="22" fill="var(--heat-orange)"/>
    <text class="brand" x="1252" y="226" font-size="15" text-anchor="middle" letter-spacing="1">MEADOWLARK PET</text>
    <text class="brand" x="1252" y="252" font-size="26" text-anchor="middle">HOSPITAL</text>
  </svg>
</main>
</body>
</html>
```